Flyer for KW Alarm Technicians

This flyer will help our technicians upsell/educate our current customers on the different service packages that we offer when the tech is in the customers home.

```html
<!DOCTYPE html>
<html lang="en">
<head>
<meta charset="utf-8">
<title>KW Alarm Technicians – Service Packages Flyer</title>
<link rel="stylesheet" href="https://fonts.googleapis.com/css2?family=Oswald:wght@500;600;700&family=Open+Sans:wght@400;600;700&display=swap">
<style>
:root{
  --blue:#1a55a0;
  --blue-dark:#134683;
  --green:#3fae3a;
  --sky:#dbe8f7;
  --ink:#222;
  --line:#2b5d9e;
  --page:#e9ebee;
  --paper:#ffffff;
}
*{box-sizing:border-box;margin:0;padding:0}
html,body{width:1200px;height:2266px;overflow:hidden;background:var(--page)}
body{position:relative;font-family:"Open Sans",sans-serif;color:var(--ink)}
.flyer{position:absolute;left:50px;top:354px;width:1100px;height:1557px;background:var(--paper);box-shadow:0 6px 24px rgba(0,0,0,.18);overflow:hidden}
.abs{position:absolute}
.brand{left:52px;top:46px;font:700 42px/1 "Open Sans",sans-serif;color:var(--blue);letter-spacing:1px}
.hero{left:0;top:115px;width:1100px;height:385px;background:linear-gradient(90deg,var(--sky) 0%,var(--sky) 30%,#b9c6c0 48%,#56654e 70%,#2f3a2e 100%)}
.hero-photo{position:absolute;left:380px;top:0;right:0;bottom:0}
.headline{left:55px;top:148px;font-family:"Oswald",sans-serif;font-weight:700;line-height:.95;text-transform:uppercase}
.headline span{display:block}
.hl-1{font-size:84px;color:var(--blue)}
.hl-2{font-size:110px;color:var(--green)}
.hl-3{font-size:122px;color:var(--blue)}
.panel{border:2px solid var(--line);background:#fff}
.devices{left:54px;top:536px;width:1000px;height:284px}
.band{background:var(--blue);color:#fff;font-family:"Oswald",sans-serif;font-weight:500;text-transform:uppercase;text-align:center}
.devices .band{height:44px;font-size:22px;line-height:44px;letter-spacing:.2px}
.band sup{color:#8fe08a;font-size:.65em}
.band .amt{color:#8fe08a}
.device-row{display:flex;height:236px}
.device{flex:1;position:relative;border-right:2px dotted var(--line)}
.device:last-child{border-right:none}
.thumb{position:absolute;border-radius:6px;background:radial-gradient(circle at 40% 40%,#f4f4f4,#a7a9ab 70%,#5b5e61)}
.device .thumb{left:14px;right:14px;top:20px;height:120px}
.pill{position:absolute;left:4px;right:4px;top:172px;height:32px;border-radius:16px;background:var(--green);color:#fff;font:700 16px/32px "Open Sans",sans-serif;text-align:center;white-space:nowrap}
.packages{left:54px;top:857px;width:998px;height:330px}
.pkg{position:absolute;top:0;width:233px;height:330px}
.pkg .band{font-size:13px;line-height:1.3;padding:10px 10px;height:82px;display:flex;align-items:center;justify-content:center}
.pkg .thumb{left:40px;right:40px;top:100px;height:95px}
.pkg-title{position:absolute;left:6px;right:6px;text-align:center;color:var(--green);font-weight:600}
.pkg-note{position:absolute;left:10px;right:10px;text-align:center;font-size:13px;line-height:1.35;color:#333}
.pkg-note b{color:var(--blue);font-weight:400}
.options{left:54px;top:1216px;width:999px;height:173px}
.opt{position:absolute;top:0;height:100%}
.opt h3{font:700 25px/1 "Open Sans",sans-serif;color:var(--blue);margin:24px 0 18px 14px}
.opt h3 sup{font-size:.55em}
.opt ul{list-style:none;margin-left:14px}
.opt li{position:relative;padding-left:26px;font-weight:700;font-size:18px;line-height:1.35;margin-bottom:10px}
.opt li svg{position:absolute;left:0;top:6px}
.divider{position:absolute;top:0;bottom:0;width:2px;background:var(--line)}
.footer{left:0;top:1420px;width:1100px;height:137px}
.foot-contact{left:52px;top:1438px;color:#fff;font-size:28px;line-height:38px;font-weight:600}
.foot-contact div{display:flex;align-items:center;gap:14px}
.foot-meta{left:595px;top:1476px;color:#fff;font-size:17px;line-height:24px}
.foot-meta div{display:flex;align-items:center;gap:10px}
.follow{left:958px;top:1476px;color:#fff;font-size:16px;border-left:2px solid #fff;padding-left:18px;line-height:24px}
.social{display:flex;gap:10px;margin-top:2px}
.social i{display:block;width:20px;height:20px;border-radius:50%;background:#fff}
</style>
</head>
<body>
<main class="flyer">
  <div class="abs brand">KW Alarm</div>

  <section class="abs hero">
    <div class="hero-photo" role="img" aria-label="Photo of a masked burglar prying open a glass patio door with a crowbar"></div>
  </section>
  <h1 class="abs headline">
    <span class="hl-1">Don’t Get</span>
    <span class="hl-2">Robbed</span>
    <span class="hl-3">Twice</span>
  </h1>

  <section class="abs panel devices">
    <div class="band">One home automation device requires a <sup>$</sup><span class="amt">6</span> a month increase per device with a 60 month renewal</div>
    <div class="device-row">
      <div class="device"><div class="thumb" role="img" aria-label="Smart doorbell camera product photo"></div><div class="pill">Smart Doorbell</div></div>
      <div class="device"><div class="thumb" role="img" aria-label="Thermostat product photo"></div><div class="pill">Thermostat</div></div>
      <div class="device"><div class="thumb" role="img" aria-label="Deadbolt door lock product photos"></div><div class="pill">Deadbolt Doorlock</div></div>
      <div class="device"><div class="thumb" role="img" aria-label="Garage door controller product photo"></div><div class="pill">Garage Controller</div></div>
      <div class="device"><div class="thumb" role="img" aria-label="Indoor camera product photo"></div><div class="pill">Smart Indoor Camera</div></div>
    </div>
  </section>

  <section class="abs packages">
    <div class="pkg panel" style="left:0">
      <div class="band">Outdoor camera requires a <sup>$</sup><span class="amt">12</span> a month increase for the camera per camera</div>
      <div class="thumb" role="img" aria-label="Outdoor camera product photo"></div>
      <div class="pkg-title" style="top:212px;font-size:17px">Smart Outdoor Camera</div>
    </div>
    <div class="pkg panel" style="left:255px">
      <div class="band">Doorbell camera and an outdoor camera requires a <sup>$</sup><span class="amt">20</span> increase a month for both these devices:</div>
      <div class="thumb" role="img" aria-label="Doorbell camera product photo"></div>
      <div class="pkg-title" style="top:210px;font-size:14px;line-height:1.3">1 outdoor camera + one other device (doorbell camera)</div>
      <div class="pkg-note" style="top:256px"><b>Requirements:</b> 60 Month Agreement Renewal + $50 Install Fee Per Outdoor Camera</div>
    </div>
    <div class="pkg panel" style="left:508px">
      <div class="band">Two or more outdoor cameras requires a <sup>$</sup><span class="amt">12</span> increase per month per outdoor camera</div>
      <div class="thumb" role="img" aria-label="Two outdoor cameras product photo"></div>
      <div class="pkg-title" style="top:214px;font-size:14px;line-height:1.3">2-4 Outdoor Cameras +<br>12 Per Camera.</div>
      <div class="pkg-note" style="top:256px"><b>Requirement:</b> +$6 5-8 cameras due to more clips package.</div>
    </div>
    <div class="pkg panel" style="left:765px">
      <div class="band">Core 2 panel upgrade requires a <sup>$</sup><span class="amt">5</span> increase per month with a 60 month renewal and a one time fee <sup>$</sup><span class="amt">100</span></div>
      <div class="thumb" role="img" aria-label="Alarm control panel product photo" style="top:112px"></div>
    </div>
  </section>

  <section class="abs panel options">
    <div class="opt" style="left:0;width:384px">
      <h3>1<sup>st</sup> Option:</h3>
      <ul>
        <li><svg width="14" height="12" viewBox="0 0 14 12"><path d="M1 6l4 4 8-9" fill="none" stroke="#1a55a0" stroke-width="2.5"/></svg>Phone line To Cell Primary No App Requires $7 Increase Per Month,</li>
        <li><svg width="14" height="12" viewBox="0 0 14 12"><path d="M1 6l4 4 8-9" fill="none" stroke="#1a55a0" stroke-width="2.5"/></svg>Also Requires A 60 Month Renewal</li>
      </ul>
    </div>
    <div class="divider" style="left:384px"></div>
    <div class="abs thumb" role="img" aria-label="Cellular communicator module with wires" style="left:400px;top:12px;width:190px;height:148px"></div>
    <div class="divider" style="left:590px"></div>
    <div class="opt" style="left:600px;width:395px">
      <h3>2<sup>nd</sup> Option:</h3>
      <ul>
        <li><svg width="14" height="12" viewBox="0 0 14 12"><path d="M1 6l4 4 8-9" fill="none" stroke="#1a55a0" stroke-width="2.5"/></svg>Phone line To Cell Primary With App Requires A $13 A Month Increase,</li>
        <li><svg width="14" height="12" viewBox="0 0 14 12"><path d="M1 6l4 4 8-9" fill="none" stroke="#1a55a0" stroke-width="2.5"/></svg>Also Requires A 60 Month Renewal</li>
      </ul>
    </div>
  </section>

  <svg class="abs footer" viewBox="0 0 1100 137" preserveAspectRatio="none">
    <rect x="0" y="34" width="1100" height="103" fill="#3fae3a"/>
    <path d="M0 0H500C540 0 560 20 575 50L610 137H0Z" fill="#1a55a0"/>
    <path d="M505 0C548 0 570 22 585 52L622 137H610L575 50C560 20 540 0 500 0Z" fill="#fff"/>
  </svg>
  <div class="abs foot-contact">
    <div><svg width="24" height="24" viewBox="0 0 24 24"><path d="M6 2l4 5-2 3c1 3 3 5 6 6l3-2 5 4-3 4C10 21 3 14 2 5z" fill="#fff"/></svg>555-014-2290</div>
    <div><svg width="24" height="24" viewBox="0 0 24 24" fill="none" stroke="#fff" stroke-width="2"><circle cx="12" cy="12" r="10"/><path d="M2 12h20M12 2c4 4 4 16 0 20M12 2c-4 4-4 16 0 20"/></svg>www.kwhomeguard.com</div>
  </div>
  <div class="abs foot-meta">
    <div><svg width="14" height="18" viewBox="0 0 14 18"><path d="M7 0a7 7 0 0 1 7 7c0 5-7 11-7 11S0 12 0 7a7 7 0 0 1 7-7z" fill="#fff"/><circle cx="7" cy="7" r="2.5" fill="#3fae3a"/></svg>PO Box 2210, Lakeview, WA 98000</div>
    <div><svg width="16" height="12" viewBox="0 0 16 12"><rect width="16" height="12" fill="#fff"/><path d="M0 0l8 6 8-6" fill="none" stroke="#3fae3a" stroke-width="1.5"/></svg>info@kwhomeguard.com</div>
  </div>
  <div class="abs follow">FOLLOW US<div class="social"><i></i><i></i><i></i></div></div>
</main>
</body>
</html>
```